【依頼の目的/概要】
電子書籍(lumora)の表紙デザインをお願いします。
【画像サイズ】※QMSより抜粋
表紙ファイルの理想的な寸法は2560×1600ピクセルです。
注:画像の寸法は1000×625ピクセル以上であることが必要です。
画像の最大の寸法は10000×10000ピクセルです。

【タイトル】
「森と響きあう内なる治癒の道」
サブキャッチ
「もうガンもウイルスも怖くない」 「30年の医療現場で私が感じたこと」
「輝く人生を送るための幸せ健康学」「歴史とデータから浮かび上がる真実」など。
【著者】
看護師30年
堀田みき

【本の内容】
病院や薬に依存し続けてきた結果の日本の現状を歴史やデータから検証。
西洋医学以前の医療に着目し自然免疫の力で健康を取り戻せることが出来ることをお伝えした本です。
※本文を参考資料として添付します。

【デザイン要望】
内容が少し専門的なのですが特に一般の方に読んでいただきたいのであまり堅苦しくない印象のものを考えてはいますが、特に要望はありませんので自由な発想でのご応募を楽しみにしています。
※次点 次々点の方への参加報酬を設定いたしました。
※その他、必要な情報がありましたらお問い合わせください。
宜しくお願いいたします。

どの作品も本当に素晴らしく最後まで悩みに悩みました。内容は医療系なのですが特に一般の方に手にとっていただきたいことから表紙と内容のギャップがないものをと思うとデザインが気に入っても、本の内容で表紙のイメージと全然違うとガッカリされないかなど考え非常に悩みました。タイトルとサブキャッチの大きさや色使い、堅苦しくない明るいデザインが私のイメージと合いましたのでtorvel様のデザインを選ばせていただきました。

今回ピクモアさんに初めて表紙の依頼をさせていただきました。デザイナーさんたちのレベルの高さに感動しておりました。
どのデザインもそれぞれが個性的で本当に素晴らしく最後の最後まで迷っておりました。
今回の本の内容と、専門的ではあるのですが一般向けにしたいということで悩んだ末そちらの視点から一点決めさせていただきました。
1点しか選べないことが心苦しいです。
皆さまお忙しい中、貴重なお時間を割いていただき本当にありがとうございました。
心から感謝しております。

```html
<!DOCTYPE html>
<html lang="ja">
<head>
<meta charset="utf-8">
<title>森と響きあう内なる治癒の道</title>
<link rel="stylesheet" href="https://fonts.googleapis.com/css2?family=Noto+Serif+JP:wght@700;900&family=Noto+Sans+JP:wght@500;700&display=swap">
<style>
  :root {
    --navy: #14285e;
    --red: #d8202a;
    --sky-top: #ffffff;
    --sky-mid: #cfe0f4;
    --deep: #0b1d4a;
    --abyss: #040c26;
    --glow: #e9f4ff;
  }
  * { margin: 0; padding: 0; box-sizing: border-box; }
  html, body { width: 750px; height: 1200px; overflow: hidden; background: #fff; }
  .cover {
    position: relative;
    width: 750px;
    height: 1200px;
    overflow: hidden;
  }
  .cover-art {
    position: absolute;
    inset: 0;
    background:
      radial-gradient(ellipse 220px 160px at 390px 800px, var(--glow) 0%, rgba(160,205,255,0.55) 35%, rgba(40,90,180,0) 100%),
      radial-gradient(ellipse 520px 420px at 330px 880px, rgba(60,120,210,0.55) 0%, rgba(20,50,120,0) 100%),
      linear-gradient(180deg, var(--sky-top) 0%, var(--sky-top) 30%, var(--sky-mid) 48%, #5f86c4 60%, var(--deep) 78%, var(--abyss) 100%);
  }
  .vertical {
    position: absolute;
    writing-mode: vertical-rl;
    text-orientation: upright;
    white-space: nowrap;
  }
  .author {
    top: 34px;
    right: 26px;
    font-family: "Noto Serif JP", serif;
    color: var(--navy);
    display: flex;
    flex-direction: column;
    align-items: center;
  }
  .author-role {
    font-size: 24px;
    font-weight: 700;
    letter-spacing: 2px;
    text-combine-upright: none;
    margin-bottom: 16px;
  }
  .author-name {
    font-size: 46px;
    font-weight: 700;
    letter-spacing: 6px;
  }
  .title-line {
    font-family: "Noto Serif JP", serif;
    font-weight: 900;
    color: var(--navy);
    font-size: 104px;
    line-height: 1;
    letter-spacing: 4px;
    top: 120px;
  }
  .title-line.first { right: 132px; }
  .title-line.second { right: 252px; }
  .title-line.accent {
    right: 372px;
    color: var(--red);
    font-size: 108px;
  }
  .catch {
    font-family: "Noto Sans JP", sans-serif;
    font-weight: 700;
    font-size: 30px;
    line-height: 1;
    letter-spacing: 2px;
    color: var(--navy);
    top: 50px;
  }
  .catch.c1 { left: 212px; top: 40px; }
  .catch.c2 { left: 164px; top: 80px; }
  .catch.c3 { left: 116px; top: 120px; }
  .catch.c4 { left: 68px; top: 160px; }
</style>
</head>
<body>
  <main class="cover">
    <div class="cover-art" role="img" aria-label="青い光の粒に包まれた人の横顔のシルエットと、胸元に輝く光"></div>

    <div class="vertical author">
      <span class="author-role">看護師30年</span>
      <span class="author-name">堀田みき</span>
    </div>

    <h1>
      <span class="vertical title-line first">森と響き</span>
      <span class="vertical title-line second">あう内なる</span>
      <span class="vertical title-line accent">治癒の道</span>
    </h1>

    <p class="vertical catch c1">もうガンもウイルスも怖くない</p>
    <p class="vertical catch c2">輝く人生を送るための幸せ健康学</p>
    <p class="vertical catch c3">30年の医療現場で私が感じたこと</p>
    <p class="vertical catch c4">歴史とデータから浮かび上がる真実</p>
  </main>
</body>
</html>
```